Small Business Consulting Firm Needs Business Card Design

Need a sleek modern business card with 2 sides matching the colors of our logo. We will be placing these with a mailer we are sending out. These business cards will only ever be given to business owners. We operate helping businesses who are struggling with cash flow or finances. If the green and blue design needs to be moved to the right of "Harborline Crest Consulting" for aesthetic purposes that is ok. We will need an editable file if possible. We would like to include the reps name, email, website, and phone number. For now just use Peter Vance, pvance@harborlinecrest.com, www.harborlinecrest.com, and 833-555-0172.

```html
<!DOCTYPE html>
<html lang="en">
<head>
<meta charset="utf-8">
<title>Harborline Crest Consulting – Business Card</title>
<link href="https://fonts.googleapis.com/css2?family=Lato:wght@400;700&display=swap" rel="stylesheet">
<style>
  :root {
    --bg-light: #e4e6e8;
    --bg-dark: #b9bcbf;
    --card: #2d2d2d;
    --white: #f4f4f4;
    --green: #76bc43;
    --green-dark: #5f9e35;
    --blue: #0a7cc4;
    --blue-dark: #0d5f9c;
  }
  * { box-sizing: border-box; margin: 0; padding: 0; }
  html, body { width: 1200px; height: 800px; overflow: hidden; }
  body {
    background: linear-gradient(135deg, var(--bg-dark) 0%, var(--bg-light) 100%);
    font-family: "Lato", sans-serif;
    position: relative;
  }
  .card {
    position: absolute;
    width: 560px;
    height: 320px;
    background: var(--card);
    box-shadow: 0 10px 24px rgba(0,0,0,.28);
    overflow: hidden;
  }
  .card--back { left: 400px; top: 50px; }
  .card--front { left: 240px; top: 420px; }

  .wordmark { color: var(--white); font-weight: 400; text-transform: uppercase; }
  .wordmark__name { display: block; letter-spacing: .12em; }
  .wordmark__sub { display: block; letter-spacing: .55em; }

  .card--back .wordmark {
    position: absolute; left: 0; right: 0; top: 120px; text-align: center;
  }
  .card--back .wordmark__name { font-size: 28px; }
  .card--back .wordmark__sub { font-size: 12px; margin-top: 6px; padding-left: .55em; }

  .stripe {
    position: absolute; left: 0; right: 0; bottom: 0; height: 10px; display: flex;
  }
  .stripe span { flex: 1; }
  .stripe .s1 { background: var(--green-dark); }
  .stripe .s2 { background: var(--green); }
  .stripe .s3 { background: var(--blue); }
  .stripe .s4 { background: var(--blue-dark); }

  .card--front .wordmark { position: absolute; left: 40px; top: 34px; }
  .card--front .wordmark__name { font-size: 22px; }
  .card--front .wordmark__sub { font-size: 10px; margin-top: 4px; padding-left: 48px; }

  .rep { position: absolute; left: 40px; top: 128px; }
  .rep__name { color: var(--green); font-size: 22px; font-weight: 700; }
  .rep__title { color: var(--white); font-size: 16px; margin-top: 2px; }

  .contact { position: absolute; left: 40px; top: 200px; list-style: none; }
  .contact li {
    display: flex; align-items: center; gap: 10px;
    color: var(--white); font-size: 15px; line-height: 24px;
  }
  .contact svg { width: 14px; height: 14px; flex: none; }

  .brand-square {
    position: absolute; right: 60px; top: 80px;
    width: 160px; height: 160px; background: var(--green);
  }
</style>
</head>
<body>

  <section class="card card--back" aria-label="Card back">
    <div class="wordmark">
      <span class="wordmark__name">Harborline Crest</span>
      <span class="wordmark__sub">Consulting</span>
    </div>
    <div class="stripe"><span class="s1"></span><span class="s2"></span><span class="s3"></span><span class="s4"></span></div>
  </section>

  <section class="card card--front" aria-label="Card front">
    <div class="wordmark">
      <span class="wordmark__name">Harborline Crest</span>
      <span class="wordmark__sub">Consulting</span>
    </div>

    <div class="rep">
      <p class="rep__name">Peter Vance</p>
      <p class="rep__title">Representative</p>
    </div>

    <ul class="contact">
      <li>
        <svg viewBox="0 0 24 24" aria-hidden="true"><path fill="#0a7cc4" d="M6.6 10.8a15.1 15.1 0 0 0 6.6 6.6l2.2-2.2c.3-.3.7-.4 1-.2 1.1.4 2.3.6 3.6.6.6 0 1 .4 1 1V20c0 .6-.4 1-1 1A17 17 0 0 1 3 4c0-.6.4-1 1-1h3.5c.6 0 1 .4 1 1 0 1.3.2 2.5.6 3.6.1.3 0 .7-.2 1z"/></svg>
        833-555-0172
      </li>
      <li>
        <svg viewBox="0 0 24 24" aria-hidden="true"><rect x="2" y="5" width="20" height="14" fill="none" stroke="#0a7cc4" stroke-width="2"/><path d="M2 5l10 8 10-8" fill="none" stroke="#0a7cc4" stroke-width="2"/></svg>
        pvance@harborlinecrest.com
      </li>
      <li>
        <svg viewBox="0 0 24 24" aria-hidden="true"><g fill="none" stroke="#0a7cc4" stroke-width="1.8"><circle cx="12" cy="12" r="9.5"/><ellipse cx="12" cy="12" rx="4" ry="9.5"/><path d="M2.5 12h19M4 7h16M4 17h16"/></g></svg>
        www.harborlinecrest.com
      </li>
    </ul>

    <div class="brand-square" aria-hidden="true"></div>
  </section>

</body>
</html>
```